Copper Ridge Stewardship Summit needs a marketing flyer

We need a full page graphic for our upcoming Forum that can also be converted into a website "header" for social media, etc.: "Copper Ridge Stewardship Summit - Making Impact Through the Built Environment"

INTRODUCTION:
During the first week of August 2022, Q-VarDT is presenting the Copper Ridge Stewardship Summit - Making Impact Through the Built Environment.

One of the most exciting aspects of this conference will be the bringing together of multiple organizations including for-profits and nonprofits, K-12’s and higher education, cities and counties and other governmental agencies, as well as architects, engineers, and contractors to collaboratively present and discuss issues and ideas related to sustainability, with a Texas focus.

This event will be a catalyst for public and private project owners to holistically gather information and momentum as we bring the resources and vision needed to achieve the goal of zero carbon emissions from the built environment by 2040, and address water, green space and the natural environment, transportation, equity, and funding, among other topics.

```html
<!DOCTYPE html>
<html lang="en">
<head>
<meta charset="utf-8">
<title>Copper Ridge Stewardship Summit – Flyer</title>
<link rel="stylesheet" href="https://fonts.googleapis.com/css2?family=Montserrat:wght@400;500;600;700;800&family=Oswald:wght@500&display=swap">
<style>
  :root {
    --stage: #b3b3b3;
    --page: #ffffff;
    --green: #8fb043;
    --green-box: #98b04a;
    --green-light: #c3d86a;
    --green-dark: #6f9a2c;
    --navy: #2f4690;
    --logo-blue: #2e4b9c;
    --ink: #3a3a3a;
    --body: #2f2f2f;
  }
  * { margin: 0; padding: 0; box-sizing: border-box; }
  html, body { width: 1047px; height: 1200px; overflow: hidden; }
  body { background: var(--stage); font-family: "Montserrat", sans-serif; position: relative; }

  .flyer { position: absolute; left: 176px; top: 161px; width: 690px; height: 897px; background: var(--page); overflow: hidden; }

  .brand { position: absolute; left: 56px; top: 36px; display: flex; align-items: center; gap: 10px; }
  .brand-dot { width: 56px; height: 56px; border-radius: 50%; background: var(--logo-blue); }
  .brand-name { font-size: 26px; font-weight: 500; color: var(--ink); letter-spacing: 0.5px; }

  .social { position: absolute; right: 52px; top: 38px; display: flex; gap: 26px; }
  .social-dot { width: 22px; height: 22px; border-radius: 50%; border: 2.5px solid var(--navy); }

  .hero-art { position: absolute; left: 56px; top: 80px; width: 580px; height: 360px; }

  .event-name { position: absolute; left: 56px; top: 451px; font-size: 20px; font-weight: 500; color: var(--ink); }
  .rule { position: absolute; left: 57px; top: 488px; width: 68px; height: 4px; background: var(--green); }
  .title { position: absolute; left: 55px; top: 498px; font-size: 40px; font-weight: 700; color: var(--green); letter-spacing: 0.5px; line-height: 48px; }
  .subtitle { position: absolute; left: 56px; top: 545px; font-size: 24px; font-weight: 700; color: var(--green); letter-spacing: 4.05px; line-height: 28px; white-space: nowrap; }

  .intro { position: absolute; left: 56px; top: 588px; width: 596px; font-size: 13.5px; line-height: 16.6px; color: var(--body); }

  .cta { position: absolute; left: 56px; top: 691px; font-size: 16px; font-weight: 700; color: var(--green); letter-spacing: 0.2px; }

  .band { position: absolute; left: 0; bottom: 0; width: 100%; height: 94px; background: var(--navy); }
  .url { position: absolute; left: 0; bottom: 12px; width: 100%; text-align: center; color: #fff; font-size: 15px; letter-spacing: 0.3px; }

  .pricing { position: absolute; left: 114px; top: 725px; width: 474px; height: 117px; background: var(--green-box); border-radius: 14px; color: #fff; }
  .tiers { display: flex; position: absolute; left: 0; top: 11px; width: 100%; height: 74px; }
  .tier { flex: 1; text-align: center; }
  .tier + .tier { border-left: 1px dotted rgba(255,255,255,0.7); }
  .tier-label { font-size: 13px; font-weight: 700; line-height: 16px; height: 35px; }
  .tier-price { font-family: "Oswald", sans-serif; font-weight: 500; font-size: 29px; line-height: 32px; }
  .offer { position: absolute; left: 0; top: 94px; width: 100%; text-align: center; font-size: 14px; line-height: 16px; letter-spacing: 0.3px; }
</style>
</head>
<body>
  <main class="flyer">
    <div class="brand">
      <span class="brand-dot"></span>
      <span class="brand-name">Q-VarDT</span>
    </div>

    <div class="social" aria-label="Social channels">
      <span class="social-dot"></span>
      <span class="social-dot"></span>
      <span class="social-dot"></span>
    </div>

    <svg class="hero-art" viewBox="0 0 580 360" role="img" aria-label="Paper-cut illustration of a green eco city with clouds, sun, wind turbines, houses and trees">
      <defs>
        <linearGradient id="heroGreen" x1="0" y1="0" x2="0" y2="1">
          <stop offset="0" stop-color="#c3d86a"/>
          <stop offset="0.6" stop-color="#a6c64a"/>
          <stop offset="1" stop-color="#6f9a2c"/>
        </linearGradient>
      </defs>
      <path d="M20 300 A275 275 0 0 1 20 80 Q60 20 160 10 Q290 -20 420 10 Q540 30 560 110 A275 275 0 0 1 550 300 Q470 250 360 280 Q220 330 20 300 Z" fill="url(#heroGreen)"/>
    </svg>

    <p class="event-name">Copper Ridge Stewardship Summit</p>
    <span class="rule"></span>
    <h1 class="title">MAKING IMPACT</h1>
    <h2 class="subtitle">THROUGH THE BUILT ENVIRONMENT</h2>

    <p class="intro">You may have added some new skills to your repertoire, or honed some old ones. You may see where our design and construction industry can make some improvements. There is a new energy in the air as we move beyond anxiety or fears that have blocked us or our organizations in the past. Now is the time to reinvent and evolve into a newer, better version of US.</p>

    <h3 class="cta">JOIN US AT THE Q-VARDT INVEST IN WOMEN FORUM:</h3>

    <div class="band"></div>
    <p class="url">www.q-vardt-events.org</p>

    <section class="pricing">
      <div class="tiers">
        <div class="tier">
          <div class="tier-label">MEMBERS</div>
          <div class="tier-price">$175</div>
        </div>
        <div class="tier">
          <div class="tier-label">NON-MEMBER</div>
          <div class="tier-price">$200</div>
        </div>
        <div class="tier">
          <div class="tier-label">GOVERNMENT<br>/NON-PROFIT</div>
          <div class="tier-price">$125</div>
        </div>
      </div>
      <p class="offer">REGISTER 2, GET ONE FREE.</p>
    </section>
  </main>
</body>
</html>
```